A4 Flyer

Bright Path Learning is starting a course in regional Victoria. We are currently advertising (See attached file A34984) in local papers but need to create a one page flyer to distribute to Aged Care facilities in the area. The A4 flyer will be inserted into a folder pack with more detailed information on Bright Path Learning. Important to use images and logoes attached

Target Market(s)

Flyer to be distributed to Aged Care facility staff and owners

Industry/Entity Type

Advertising

Font styles to use
Sans Serif

Colors
f37123
ec1f27

Requirements
Must have
• BPL Logo
Some image

```html
<!DOCTYPE html>
<html lang="en">
<head>
<meta charset="utf-8">
<title>Bright Path Learning – Fast Track Course Flyer</title>
<link rel="stylesheet" href="https://fonts.googleapis.com/css2?family=Jost:ital,wght@0,400;0,600;0,700;1,400&display=swap">
<style>
  :root {
    --orange: #f05a28;
    --brand-orange: #f37123;
    --yellow: #f9c21b;
    --white: #ffffff;
    --paper: #f4f4f2;
    --ink: #4a4a4c;
    --photo-light: #e9e6e3;
    --photo-mid: #b9a79b;
    --photo-dark: #2a2526;
  }
  * { margin: 0; padding: 0; box-sizing: border-box; }
  html, body { width: 848px; height: 1200px; overflow: hidden; background: var(--paper); }
  body { font-family: "Jost", "Futura", sans-serif; }
  .flyer { position: relative; width: 848px; height: 1200px; overflow: hidden; background: var(--paper); }

  .photo {
    position: absolute; left: 0; top: 380px; width: 400px; height: 820px;
    background: linear-gradient(180deg, var(--photo-light) 0%, var(--photo-mid) 35%, var(--photo-dark) 70%, var(--photo-light) 100%);
  }

  .brand {
    position: absolute; left: 40px; top: 200px; width: 290px;
    display: flex; align-items: center; gap: 14px;
    color: var(--brand-orange); font-weight: 400; font-size: 40px; line-height: 1.05;
  }
  .brand-dot { width: 26px; height: 26px; border-radius: 50%; background: var(--brand-orange); flex: none; }

  .panel { position: absolute; inset: 0; width: 848px; height: 1200px; }

  .copy { position: absolute; left: 368px; width: 480px; text-align: center; color: var(--white); }
  .yellow { color: var(--yellow); }

  .headline { top: 98px; line-height: 1; }
  .headline .lead { display: block; font-size: 62px; font-weight: 400; color: var(--yellow); }
  .headline .main { display: block; font-size: 52px; font-weight: 700; margin-top: 2px; }

  .course { top: 230px; font-size: 23px; line-height: 27px; }
  .course strong { font-weight: 700; }
  .venue { top: 314px; font-size: 23px; line-height: 26px; }

  .qualification { top: 446px; font-size: 26px; line-height: 29px; font-weight: 400; text-transform: uppercase; padding: 0 40px; }
  .qualification strong { font-weight: 700; }

  .funding { top: 598px; font-size: 24px; line-height: 29px; padding: 0 60px; }
  .funding em { font-style: italic; }

  .enrol { top: 718px; font-size: 23px; line-height: 28px; }
  .enrol h2 { font-size: 35px; font-weight: 700; color: var(--yellow); line-height: 44px; letter-spacing: 0.5px; }

  .delivery { top: 846px; font-size: 22px; line-height: 28px; padding: 0 50px; }

  .topics { top: 964px; font-size: 23px; line-height: 32px; padding: 0 30px; }
  .topics .sep { color: var(--yellow); margin: 0 6px; }
</style>
</head>
<body>
<main class="flyer">
  <div class="photo" role="img" aria-label="Photo of a smiling student seated at a desk with papers, classmates blurred in the background"></div>

  <div class="brand">
    <span class="brand-dot"></span>
    <span>bright path<br>learning</span>
  </div>

  <svg class="panel" viewBox="0 0 848 1200" aria-hidden="true">
    <path d="M402 0 C385 120 370 250 368 430 L368 570 C366 800 340 1000 322 1200 L848 1200 L848 0 Z" fill="var(--orange)"/>
    <rect x="368" y="428" width="480" height="4" fill="var(--white)"/>
    <rect x="368" y="568" width="480" height="4" fill="var(--white)"/>
  </svg>

  <header class="copy headline">
    <span class="lead">Unique</span>
    <span class="main">Opportunity</span>
  </header>

  <p class="copy course"><strong>Fast Track Course</strong><br>- Start July <span class="yellow">2014</span></p>

  <p class="copy venue">Wattle Grove Nursing<br>Home - Stawell<br><span class="yellow">9:00am - 3:00pm</span></p>

  <p class="copy qualification"><strong>Double Qualification - Cert III</strong> in Aged Care with Home and Community Care</p>

  <p class="copy funding">Government Funding for eligible students! <em>Fees from $117</em></p>

  <div class="copy enrol">
    <h2>TO ENROL VISIT</h2>
    <p>brightpathlearning.com.au<br>OR CALL 9555 0142</p>
  </div>

  <p class="copy delivery">This training is delivered with VIC and Comm Govt Funding to eligible students</p>

  <p class="copy topics">
    Pathology<span class="sep">•</span>Aged Care<br>
    First Aid<span class="sep">•</span>CPR<span class="sep">•</span>Anaphylaxis<br>
    <span class="sep">•</span>Home &amp; Community Care<span class="sep">•</span><br>
    Medications for PCA's Health Services
  </p>
</main>
</body>
</html>
```